Logistics and freight company requires website

Hi, a logistic and freight company which is based in the United States needs an industry standard website for its activities. We are into forwarding and courier goods from within United States and Canada. We deliver a wide range of goods from shipping of electronics to document, clothings, etc. The proposed website should be comtemporary and youthful. I require brilliant colors for the website. The website should be the basic things of a site. There should a category for shipping electronics, clothings, documents and others( stuffs not listed within the three I mentioned).

```html
<!DOCTYPE html>
<html lang="en">
<head>
<meta charset="utf-8">
<title>Freightly – Trucking and Transport</title>
<link href="https://fonts.googleapis.com/css2?family=Roboto:wght@400;500;700&family=Titillium+Web:wght@600;700&display=swap" rel="stylesheet">
<style>
:root{
  --backdrop:#c6c6c6;
  --navy:#14508f;
  --navy-dark:#103e70;
  --navy-band:#1a5ca3;
  --teal:#12b8e6;
  --red:#ff3344;
  --orange:#ff8a1f;
  --ink:#2c3540;
  --muted:#9a9a9a;
  --line:#e6e6e6;
  --topbar:#f4f4f4;
  --field:#f3f3f3;
  --icon:#12b8e6;
}
*{box-sizing:border-box;margin:0;padding:0}
html,body{width:960px;height:1200px;overflow:hidden;background:var(--backdrop)}
.stage{width:1200px;height:1500px;transform:scale(.8);transform-origin:0 0;position:relative;font-family:"Roboto",sans-serif;color:var(--ink)}
.page{position:absolute;left:205px;top:6px;width:756px;height:1494px;background:#fff;overflow:hidden}
.abs{position:absolute}
.heading{font-family:"Titillium Web",sans-serif;font-weight:700;color:var(--ink);letter-spacing:-.3px;line-height:1}

.topbar{left:0;top:0;width:756px;height:20px;background:var(--topbar);font-size:7px;color:var(--muted)}
.topbar .welcome{left:59px;top:6px}
.topbar .links{right:57px;top:6px;display:flex;gap:17px}

.brand-mark{left:113px;top:30px;width:14px;height:14px;border-radius:50%;background:var(--teal)}
.brand{left:91px;top:48px;font-family:"Titillium Web",sans-serif;font-weight:700;font-size:17px;color:var(--navy)}
.contact{top:35px;font-size:7px;color:var(--muted)}
.contact b{display:block;font-size:8px;color:var(--ink);margin-top:5px;font-weight:500}
.contact svg{vertical-align:-1px;margin-right:3px}
.divider{top:33px;width:1px;height:28px;background:var(--line)}
.btn{display:flex;align-items:center;justify-content:center;font-size:7.5px;font-weight:700;text-transform:uppercase;color:#fff;background:var(--teal)}
.quote-btn{left:596px;top:33px;width:102px;height:24px}

.navbar{left:0;top:71px;width:756px;height:33px;background:var(--navy)}
.nav-notch{left:0;top:71px;width:228px;height:17px;background:#fff;clip-path:polygon(0 0,100% 0,91% 100%,0 100%)}
.nav{left:244px;top:83px;display:flex;gap:22px;font-size:8.5px;font-weight:700;color:#fff}
.nav .active{position:relative}
.nav .active::after{content:"";position:absolute;left:0;right:0;bottom:-9px;height:2px;background:var(--red)}
.social{left:594px;top:77px;display:flex;gap:5px}
.social span{width:22px;height:22px;background:rgba(255,255,255,.25);display:block}

.hero{left:0;top:104px;width:756px;height:233px;background:linear-gradient(110deg,#1d2d40 0%,#22374e 40%,#3a5370 70%,#1f3048 100%)}
.arrows{left:59px;top:127px;display:flex;gap:2px}
.arrows span{width:22px;height:22px;background:rgba(255,255,255,.3);display:flex;align-items:center;justify-content:center}
.hero-title{left:59px;top:168px;font-size:23px;color:#fff;line-height:27px;text-transform:uppercase}
.hero-title .dot{color:var(--red)}
.hero-text{left:59px;top:230px;width:310px;font-size:8.5px;line-height:14.5px;color:#fff}
.hero-btn1{left:61px;top:272px;width:88px;height:24px}
.hero-btn2{left:152px;top:272px;width:86px;height:24px;background:#fff;color:var(--ink)}

.welcome-card{left:49px;top:362px;width:147px;height:254px;background:#fff;box-shadow:0 1px 6px rgba(0,0,0,.15);padding:20px 16px;border-top:3px solid var(--teal)}
.welcome-card h2{font-size:14px;line-height:16px;text-transform:uppercase}
.body-text{font-size:7.4px;line-height:12.5px;color:var(--muted)}
.welcome-card p{margin-top:18px}
.more{font-size:7.5px;font-weight:700;color:var(--teal);text-transform:uppercase}
.more::after{content:" ▸";font-size:6px}
.welcome-card .more{margin-top:8px;display:block}

.feature{top:362px;width:147px}
.feature .photo{height:98px}
.feature h3{font-size:14px;text-transform:uppercase;margin-top:17px}
.feature p{margin-top:9px;height:86px}
.feature .more{display:block;margin-top:8px}

.section-title{font-size:23px;text-transform:uppercase}
.rule{height:1px;background:var(--line)}

.service{width:201px;height:67px;border:1px solid var(--line);box-shadow:0 1px 2px rgba(0,0,0,.08);padding:16px 17px;border-left:3px solid var(--teal)}
.service h4{font-size:8px;font-weight:700;text-transform:uppercase;color:var(--ink)}
.service p{font-size:7px;line-height:10px;color:var(--muted);margin-top:6px;width:135px}
.service svg{position:absolute;right:16px;top:22px}
.service.hot{border-left-color:var(--orange)}
.service.hot svg *{fill:var(--orange)}

.about-text p{margin-bottom:7px}
.quote-card{left:379px;top:919px;width:311px;height:232px;background:#fff;box-shadow:0 1px 6px rgba(0,0,0,.15);padding:18px 16px;border-top:3px solid var(--teal)}
.quote-card h2{font-size:14px;text-transform:uppercase}
.quote-card p{margin-top:15px;width:285px}
.field{position:absolute;background:var(--field);border:1px solid #ececec;font-size:7px;color:#bbb;padding:8px}
.send-btn{left:202px;top:189px;width:93px;height:25px}

.map{left:0;top:1219px;width:756px;height:212px;background:radial-gradient(ellipse at 60% 45%,#e4e4e4 0%,#d6d6d6 35%,#2a64a3 70%,#14508f 100%)}
.footer{left:0;top:1431px;width:756px;height:63px;background:var(--navy-dark)}
.footer-band{left:0;top:1431px;width:756px;height:32px;background:var(--navy-band);clip-path:polygon(0 0,100% 0,100% 100%,6% 100%,3% 100%)}
.copyright{right:54px;top:1475px;font-size:7.5px;color:#8fb0d2}
</style>
</head>
<body>
<div class="stage">
<div class="page">

  <div class="abs topbar">
    <span class="abs welcome">Welcome to our land of opportunities</span>
    <div class="abs links"><span>Extras</span><span>Buy Now</span><span>Theme Documentation</span></div>
  </div>

  <span class="abs brand-mark"></span>
  <span class="abs brand">Freightly</span>

  <div class="abs contact" style="left:313px">
    <svg width="7" height="7" viewBox="0 0 10 10"><path d="M1 4a4 4 0 0 1 8 0v3H7V4H3v3H1z" fill="#ff3344"/></svg>Call Us Anytime<b>1-800-555-0142</b>
  </div>
  <span class="abs divider" style="left:392px"></span>
  <div class="abs contact" style="left:409px">
    <svg width="7" height="7" viewBox="0 0 10 10"><circle cx="5" cy="5" r="4" fill="none" stroke="#ff3344" stroke-width="1.5"/><path d="M5 2.5V5h2" stroke="#ff3344" fill="none"/></svg>Opening Time<b>08:00 - 18:00</b>
  </div>
  <span class="abs divider" style="left:484px"></span>
  <div class="abs contact" style="left:499px">
    <svg width="8" height="7" viewBox="0 0 10 8"><rect x=".5" y=".5" width="9" height="7" fill="none" stroke="#ff3344"/><path d="M.5 .5 5 4.5 9.5.5" fill="none" stroke="#ff3344"/></svg>Email Us<b>info@freightly.com</b>
  </div>
  <div class="abs btn quote-btn">Request a Quote</div>

  <div class="abs navbar"></div>
  <div class="abs nav-notch"></div>
  <nav class="abs nav">
    <span class="active">Home</span><span>Services ▾</span><span>About Us</span><span>Shop</span><span>News</span><span>Contact Us</span>
  </nav>
  <div class="abs social"><span></span><span></span><span></span><span></span></div>

  <div class="abs hero" role="img" aria-label="Truck driving on a highway under a stormy sky"></div>
  <div class="abs arrows">
    <span><svg width="5" height="6" viewBox="0 0 5 6"><path d="M4 0 0 3 4 6z" fill="#fff"/></svg></span>
    <span><svg width="5" height="6" viewBox="0 0 5 6"><path d="M1 0 5 3 1 6z" fill="#fff"/></svg></span>
  </div>
  <h1 class="abs heading hero-title">Unbeatable trucking and<br>transport services<span class="dot">.</span></h1>
  <p class="abs hero-text">Starting from loading to unloading and maintaining the highest standards in terms of safety while in transit, we take nothing to chance.</p>
  <div class="abs btn hero-btn1">Our Services</div>
  <div class="abs btn hero-btn2">Get in Touch</div>

  <div class="abs welcome-card">
    <h2 class="heading">Hello there<br>and welcome</h2>
    <p class="body-text">Our warehousing services are known nationwide to be one of the most reliable, safe and affordable, because we take pride in delivering the best of warehousing services, at the most reasonable prices. Our own warehouses, as well as our partner's warehouses are located at strategic locations to ensure that there is no additional cost.</p>
    <span class="more">More about us</span>
  </div>

  <div class="abs feature" style="left:213px">
    <div class="photo" role="img" aria-label="Freight train crossing a desert" style="background:linear-gradient(180deg,#3f8fd6 0%,#a9cbe6 50%,#8a6a4c 100%)"></div>
    <h3 class="heading">Cargo</h3>
    <p class="body-text">Team of cargo experts are always available to help you with any queries you might have, or if you want to consult in length your logistic requirements. We would study your requirements and provide you with a quote that would not only suit your ...</p>
    <span class="more">Read more</span>
  </div>
  <div class="abs feature" style="left:377px">
    <div class="photo" role="img" aria-label="Container port with cranes and a plane overhead" style="background:linear-gradient(180deg,#1f86e0 0%,#6fb8f0 45%,#f0622e 75%,#2a63b0 100%)"></div>
    <h3 class="heading">Logistic Service</h3>
    <p class="body-text">We provide logistic services in the nation, whether it is freight transportation, supply chain solutions, warehousing and distribution, customer resource area services, customs, security and insurance, temperature controlled logistics, industry ...</p>
    <span class="more">Read more</span>
  </div>
  <div class="abs feature" style="left:541px">
    <div class="photo" role="img" aria-label="Warehouse aisle lined with stacked shelves" style="background:linear-gradient(90deg,#6b4a2a 0%,#e0b77e 50%,#6b4a2a 100%)"></div>
    <h3 class="heading">Storage</h3>
    <p class="body-text">We take pride in catering to a broad range of clientele throughout the country with our warehousing services, which is comprehensive, reliable and flexible – qualities that are essential to help businesses in this market. Our experienced experts ...</p>
    <span class="more">Read more</span>
  </div>

  <h2 class="abs heading section-title" style="left:53px;top:654px">Our Services</h2>
  <div class="abs rule" style="left:216px;top:664px;width:474px"></div>

  <div class="abs service" style="left:53px;top:698px">
    <h4>Electronics Shipping</h4><p>Phones, laptops and gadgets packed and shipped safely.</p>
    <svg width="26" height="20" viewBox="0 0 26 20"><rect x="3" y="0" width="20" height="14" rx="1" fill="var(--icon)"/><rect x="5.5" y="2.5" width="15" height="9" fill="#fff"/><path d="M0 16h26l-2 4H2z" fill="var(--icon)"/></svg>
  </div>
  <div class="abs service hot" style="left:272px;top:698px">
    <h4>Clothing Shipping</h4><p>Apparel and textiles moved fast from point A to point B.</p>
    <svg width="26" height="22" viewBox="0 0 26 22"><path d="M9 0h8l9 5-3 6-4-2v13H7V9l-4 2-3-6z" fill="var(--icon)"/></svg>
  </div>
  <div class="abs service" style="left:490px;top:698px">
    <h4>Document Courier</h4><p>Letters and papers delivered across the US and Canada.</p>
    <svg width="20" height="24" viewBox="0 0 20 24"><path d="M0 0h13l7 7v17H0z" fill="var(--icon)"/><rect x="4" y="11" width="12" height="2" fill="#fff"/><rect x="4" y="15" width="12" height="2" fill="#fff"/><rect x="4" y="19" width="8" height="2" fill="#fff"/></svg>
  </div>
  <div class="abs service hot" style="left:53px;top:783px">
    <h4>Other Goods</h4><p>Anything not listed above? We ship it with the same care.</p>
    <svg width="24" height="22" viewBox="0 0 24 22"><rect x="0" y="0" width="24" height="6" fill="var(--icon)"/><rect x="1.5" y="7" width="21" height="15" fill="var(--icon)"/><rect x="8" y="10" width="8" height="2.5" fill="#fff"/></svg>
  </div>
  <div class="abs service" style="left:272px;top:783px">
    <h4>Door-to-door delivery</h4><p>Do you need something delivered? We are what you are looking for!</p>
    <svg width="24" height="20" viewBox="0 0 24 20"><path d="M12 0 0 10h3v10h7v-6h4v6h7V10h3z" fill="var(--icon)"/></svg>
  </div>
  <div class="abs service hot" style="left:490px;top:783px">
    <h4>Ground Transport</h4><p>Transport your things with our super moving vans.</p>
    <svg width="26" height="20" viewBox="0 0 26 20"><path d="M7 0h12l7 20h-9l-1-5h-6l-1 5H0z" fill="var(--icon)"/><rect x="12" y="3" width="2" height="3" fill="#fff"/><rect x="12" y="8" width="2" height="3" fill="#fff"/></svg>
  </div>

  <h2 class="abs heading section-title" style="left:50px;top:921px">About Us</h2>
  <div class="abs rule" style="left:166px;top:932px;width:196px"></div>
  <div class="abs about-text body-text" style="left:50px;top:962px;width:312px">
    <p>But i must explain to you how all this mistaken idea of denouncing pleasure and praising pain was born and I will give you a complete count of the system, and expound the actual teaings of the great explorer idea announcing. But i must explain to you how all this mistaken idea of denouncing pleasure and praising pain was born and I will give you a complete count of the system, and expound the actual teaings of the great explorer idea announcing.</p>
    <p>But i must explain to you how all this mistaken idea of denouncing pleasure and praising pain was born and i will give you a complete count of the system, and expound the actual teaings of the great explorer idea announcing.</p>
    <span class="more">Read more</span>
  </div>

  <div class="abs quote-card">
    <h2 class="heading">Request a quick quote</h2>
    <p class="body-text">But i must explain to you how all this mistaken idea of denouncing pleasure and praising pain was born and I will give you a complete count.</p>
    <div class="field" style="left:16px;top:87px;width:131px;height:26px">First and Last Name</div>
    <div class="field" style="left:163px;top:87px;width:132px;height:26px">Subject</div>
    <div class="field" style="left:16px;top:121px;width:131px;height:26px">E-mail address</div>
    <div class="field" style="left:163px;top:121px;width:132px;height:60px">Message</div>
    <div class="field" style="left:16px;top:155px;width:131px;height:26px;color:#888">Transport<span style="position:absolute;right:0;top:0;width:10px;height:24px;border-left:1px solid #ccc;font-size:6px;text-align:center;line-height:24px">▾</span></div>
    <div class="abs btn send-btn">Send Message</div>
  </div>

  <div class="abs map" role="img" aria-label="Map of the coastline with an office location marker"></div>

  <div class="abs footer"></div>
  <div class="abs footer-band"></div>
  <span class="abs copyright">Copyright © 2009–2015 Northway Net. All rights reserved.</span>

</div>
</div>
</body>
</html>
```